Adult Literacy Program - flyer to attract volunteers and students

We want a flyer that is engaging, colorful, modern and will appeal to our primary audience of adults aged 40-60. We are trying to attract both prospective volunteers (typically age 50+, mostly women) and students (typically aged 40+).
The flyer should feature diverse people working together in pairs of two, reading or talking, with a workbook or some reading material in front of them.

Our organization trains tutors to work one-on-one with adults who are learning how to read. Most of our adult students are non-native speakers of English. Many are of Haitian or Hispanic origin, so we would like some people who represent that demographic.

The Flyer should represent reading, learning, literacy, knowledge, growth,
and opportunities.
Our students are learning to read so they can advance their job opportunities.

Target Market(s)

Adults aged 40-60, primarily women, retired, volunteers

Industry/Entity Type

Education

Font styles to use
Serif
Sans Serif

Colors

Designer to choose colors to be used in the design.

Requirements
Must have
• - UPDATE: Should be designed as a TRI-FOLD brochure on 8.5 x 11 inch paper that will be folded into thirds.
• - Images of diverse people, women and men, who look Hispanic, Haitian and other nationalities as well as Caucasian.
• - Our logo on the front cover
Nice to have
• The sample flyer is very boring and dry! We are open to different ways of presenting the text.

```html
<!DOCTYPE html>
<html lang="en">
<head>
<meta charset="utf-8">
<title>Adult Literacy Program – Tutors and Students</title>
<link rel="stylesheet" href="https://fonts.googleapis.com/css2?family=Oswald:wght@500&family=Lato:ital,wght@0,400;0,700;1,400&display=swap">
<style>
  :root {
    --mint: #e9fcef;
    --coral: #f06868;
    --ink: #1f1f1f;
    --heading: #3b3b3b;
    --white: #ffffff;
  }
  * { margin: 0; padding: 0; box-sizing: border-box; }
  html, body { width: 927px; height: 1200px; overflow: hidden; }
  body { background: var(--mint); font-family: 'Lato', sans-serif; color: var(--ink); position: relative; }

  .bookshelf-band {
    position: absolute; left: 0; top: 0; width: 927px; height: 165px;
    background: linear-gradient(90deg, #6b4a32, #8a6a45 18%, #4f5a48 35%, #9a7b56 52%, #5e3f2c 70%, #8c7355 85%, #6a2f36);
  }

  .panel {
    position: absolute; left: 52px; width: 822px;
    background: var(--white); border: 3px solid var(--coral);
    overflow: hidden;
  }
  .panel--tutors { top: 50px; height: 507px; }
  .panel--students { top: 633px; height: 537px; }

  .panel__content {
    position: absolute; width: var(--w); height: 822px;
    left: calc((822px - var(--w)) / 2 - 3px);
    top: calc((var(--h) - 822px) / 2 - 3px);
    transform: rotate(90deg);
    display: flex; flex-direction: column; align-items: center; text-align: center;
  }
  .panel--tutors .panel__content { --w: 507px; --h: 507px; }
  .panel--students .panel__content { --w: 537px; --h: 537px; }

  .panel__title {
    font-family: 'Oswald', sans-serif; font-weight: 500;
    font-size: 58px; letter-spacing: 8px; color: var(--heading);
    margin-top: 42px; line-height: 72px;
  }
  .panel__rule { width: 284px; height: 3px; background: var(--coral); margin-top: 10px; }

  .facts { list-style: none; margin-top: 40px; font-size: 22px; line-height: 29px; }
  .facts li { margin-bottom: 22px; padding: 0 40px; }
  .facts em { font-style: italic; }

  .tagline {
    position: relative; margin-top: 60px; width: 507px; height: 92px;
  }
  .tagline__text {
    position: absolute; left: 80px; right: 80px; top: 18px;
    color: var(--coral); font-weight: 700; font-size: 23px; line-height: 29px;
  }
  .tagline svg { position: absolute; left: 0; top: 0; }

  .students-photo {
    position: absolute; left: 8px; right: 8px; bottom: 9px; height: 293px;
    background: linear-gradient(135deg, #c9a5a8 0%, #e7e4df 35%, #d9d6d0 60%, #8c8a86 100%);
  }
</style>
</head>
<body>
  <div class="bookshelf-band" role="img" aria-label="Photo of old books on a shelf"></div>

  <section class="panel panel--tutors">
    <div class="panel__content">
      <h2 class="panel__title">TUTORS</h2>
      <div class="panel__rule"></div>
      <ul class="facts">
        <li>No special skills or degrees needed just a degree of caring!</li>
        <li>Training offered throughout the year</li>
        <li>Tutors meet students weekly at a library</li>
        <li>Instructional materials provided</li>
        <li>Ongoing support available</li>
      </ul>
      <div class="tagline">
        <svg width="507" height="92" viewBox="0 0 507 92" fill="none" stroke="#1f1f1f" stroke-width="2.5">
          <path d="M86 2 H72 V90 H86 M72 46 H12"/>
          <path d="M421 2 H435 V90 H421 M435 46 H495"/>
        </svg>
        <p class="tagline__text">Teach an adult to read and you'll change a life forever.</p>
      </div>
    </div>
  </section>

  <section class="panel panel--students">
    <div class="panel__content">
      <h2 class="panel__title">STUDENTS</h2>
      <div class="panel__rule"></div>
      <ul class="facts">
        <li>Students are adults in need of <em>basic literacy skills, pre GED skills, conversational English</em></li>
        <li>Tutoring is free of charge</li>
        <li>Tutoring is one-on-one</li>
        <li>Flexible scheduling during library hours</li>
        <li>Lessons focus on student goals</li>
      </ul>
      <div class="students-photo" role="img" aria-label="Photo of a tutor and an adult student working together at a library table"></div>
    </div>
  </section>
</body>
</html>
```